Caldrow Supplies Business Card

Professional business card that stand out to our potential customers. Front and back with clean modern design

Industry/Entity Type

Oil and gas

Contact Information for Business Card

Name, address, website , office phone and cell number

Requirements
Must have
• Editable files for each employee

```html
<!DOCTYPE html>
<html lang="en">
<head>
<meta charset="utf-8">
<title>Caldrow Supplies Business Card</title>
<link rel="stylesheet" href="https://fonts.googleapis.com/css2?family=Fira+Sans:wght@600&family=Montserrat:wght@400;500;700&display=swap">
<style>
  :root {
    --bg: #e7e5e7;
    --paper: #ffffff;
    --brand-red: #e8231f;
    --brand-blue: #0aafd0;
    --ink: #1b1b1b;
  }
  * { margin: 0; padding: 0; box-sizing: border-box; }
  html, body { width: 1200px; height: 1108px; overflow: hidden; }
  body {
    background: var(--bg);
    font-family: "Montserrat", Arial, sans-serif;
    color: var(--ink);
    position: relative;
  }
  .card { position: absolute; left: 222px; width: 786px; }
  .card-front { top: 51px; height: 479px; background: var(--paper); }
  .card-back { top: 577px; height: 462px; background: var(--brand-blue); }

  .brand-mark {
    position: absolute;
    display: flex; align-items: center; gap: 10px;
    font-family: "Montserrat", Arial, sans-serif;
    font-weight: 700;
    white-space: nowrap;
  }
  .brand-mark .brand-square { display: block; flex: none; }
  .card-front .brand-mark {
    left: 92px; top: 214px; font-size: 26px; color: var(--brand-red);
  }
  .card-front .brand-mark .brand-square { width: 22px; height: 22px; background: var(--brand-red); }
  .card-back .brand-mark {
    left: 0; right: 0; top: 200px; justify-content: center;
    font-size: 46px; color: var(--paper); gap: 16px;
  }
  .card-back .brand-mark .brand-square { width: 38px; height: 38px; background: var(--paper); }

  .divider {
    position: absolute; left: 385px; top: 144px;
    width: 2px; height: 192px; background: var(--brand-red);
  }
  .person { position: absolute; left: 406px; top: 138px; }
  .person-name {
    font-family: "Fira Sans", Arial, sans-serif;
    font-weight: 600; font-size: 31px; color: var(--brand-red); line-height: 1.1;
  }
  .person-title { font-size: 18px; margin-top: 6px; }
  .contact-list { list-style: none; margin-top: 20px; }
  .contact-list li {
    display: flex; align-items: center; gap: 8px;
    font-size: 18px; height: 30.5px;
  }
  .contact-list svg { width: 17px; height: 17px; fill: var(--brand-blue); flex: none; }
  .address {
    position: absolute; left: 0; right: 0; top: 395px;
    text-align: center; font-size: 18px;
  }
</style>
</head>
<body>
  <section class="card card-front">
    <div class="brand-mark"><span class="brand-square"></span>Caldrow Supplies</div>
    <div class="divider"></div>
    <div class="person">
      <h1 class="person-name">Tarek Halloum</h1>
      <p class="person-title">President</p>
      <ul class="contact-list">
        <li>
          <svg viewBox="0 0 24 24" aria-hidden="true"><path d="M3 9c0-3 4-5 9-5s9 2 9 5v2h-5V8.5c-1-.6-2.5-.9-4-.9s-3 .3-4 .9V11H3z"/><path d="M5 20l2-8h10l2 8z M12 13.5a2.5 2.5 0 1 0 0 5 2.5 2.5 0 0 0 0-5z" fill-rule="evenodd"/></svg>
          +1.555.214.0300 x210
        </li>
        <li>
          <svg viewBox="0 0 24 24" aria-hidden="true"><path d="M6.6 10.8a15 15 0 0 0 6.6 6.6l2.2-2.2c.3-.3.7-.4 1-.2 1.1.4 2.3.6 3.6.6.6 0 1 .4 1 1V20c0 .6-.4 1-1 1A17 17 0 0 1 3 4c0-.6.4-1 1-1h3.5c.6 0 1 .4 1 1 0 1.3.2 2.5.6 3.6.1.3 0 .7-.2 1z"/><path d="M14 3a7 7 0 0 1 7 7h-1.6A5.4 5.4 0 0 0 14 4.6zm0 3a4 4 0 0 1 4 4h-1.6A2.4 2.4 0 0 0 14 7.6z"/></svg>
          +1.555.860.412
        </li>
        <li>
          <svg viewBox="0 0 24 24" aria-hidden="true"><path d="M2 6h20v1.5l-10 6-10-6z M2 9.5l10 6 10-6V19H2z"/></svg>
          info@caldrowsupplies.com
        </li>
        <li>
          <svg viewBox="0 0 24 24" aria-hidden="true"><path d="M12 2a10 10 0 1 0 0 20 10 10 0 0 0 0-20zm-1 17.9A8 8 0 0 1 4.2 10L9 14.8v1.1c0 1.1.9 2 2 2zm6.9-2.5c-.3-.8-1-1.4-1.9-1.4h-1v-3c0-.6-.4-1-1-1H8v-2h2c.6 0 1-.4 1-1V7h2c1.1 0 2-.9 2-2v-.4a8 8 0 0 1 2.9 12.8z"/></svg>
          www.caldrowsupplies.com
        </li>
      </ul>
    </div>
    <p class="address">240 Meridian Plaza Westbrook, NJ 07930 USA</p>
  </section>

  <section class="card card-back">
    <div class="brand-mark"><span class="brand-square"></span>Caldrow Supplies</div>
  </section>
</body>
</html>
```